The First Annual Fernwick Legacy Gala

Something similar to the attached but an attention grabber. It needs to attract people with money to spend!

```html
<!DOCTYPE html>
<html lang="en">
<head>
<meta charset="utf-8">
<title>The First Annual Fernwick Legacy Gala</title>
<link href="https://fonts.googleapis.com/css2?family=Oswald:wght@500;600&family=Raleway:wght@400;500;700;800&display=swap" rel="stylesheet">
<style>
:root{
  --blue:#7b9fd8;
  --blue-deep:#6a8fcc;
  --dark:#353535;
  --mid:#5b5b5b;
  --light:#ececec;
  --white:#ffffff;
  --ink:#2b2b2b;
  --stage:#5e5e5e;
}
*{margin:0;padding:0;box-sizing:border-box}
html,body{width:1200px;height:2853px;overflow:hidden;background:var(--stage)}
.flyer{
  position:absolute;left:40px;top:635px;width:808px;height:1142px;
  transform:scale(1.386);transform-origin:top left;
  background:var(--white);overflow:hidden;
  font-family:"Raleway",Arial,sans-serif;color:var(--ink);
  box-shadow:0 8px 24px rgba(0,0,0,.35);
}
.abs{position:absolute}
.band-left{left:0;top:0;width:157px;height:300px;background:var(--blue)}
.band-right{left:651px;top:0;width:157px;height:330px;background:var(--blue)}
.venue-photo{left:0;top:230px;width:808px;height:360px;
  background:linear-gradient(165deg,#b9cde9 0%,#dfe6ef 45%,#eef1f4 70%,#d3d9e0 100%);
  clip-path:polygon(0 0,157px 0,157px 40px,651px 40px,651px 80px,100% 80px,100% 100%,0 100%)}
.title-panel{left:157px;top:0;width:494px;height:420px;background:var(--dark);text-align:center;
  clip-path:polygon(0 0,100% 0,100% 100%,0 285px)}
.presents{margin-top:40px;color:var(--blue);font-size:15.5px;font-weight:500;letter-spacing:.2px}
.title{font-family:"Oswald",Impact,sans-serif;font-weight:600;line-height:1.04;margin-top:18px}
.title .lead{display:block;color:var(--white);font-size:58px}
.title .name{display:block;color:var(--blue);font-size:58px}
.wave{left:0;top:470px;width:808px;height:180px}
.date-badge{left:458px;top:432px;width:268px;height:268px}
.date-text{left:458px;top:492px;width:268px;text-align:center;color:var(--white)}
.date-text .day{font-family:"Oswald",Impact,sans-serif;font-weight:600;font-size:50px;line-height:1}
.date-text .year{font-size:24px;font-weight:500;letter-spacing:9px;margin-top:3px;padding-left:9px;line-height:1.1}
.date-text .time{font-size:18px;font-weight:800;line-height:1.2;margin-top:18px}
.headline{left:30px;top:584px;width:370px;color:var(--blue);font-weight:800;font-size:31px;line-height:1.1}
.rule{left:31px;top:696px;width:84px;height:3px;background:var(--dark)}
.body-copy{left:31px;top:720px;width:350px;font-size:12.6px;line-height:1.42;text-align:justify;color:var(--ink)}
.body-copy p{margin-bottom:9px}
.ticket-box{left:430px;top:718px;width:336px;height:185px;border:2px solid var(--blue);border-radius:8px;overflow:hidden;text-align:center}
.ticket-box .price{background:var(--mid);color:var(--white);padding:6px 0 7px}
.ticket-box .price small{display:block;font-size:14px;font-weight:500}
.ticket-box .price strong{display:block;font-size:24px;font-weight:800;line-height:1.15}
.ticket-box .raffle{font-size:14px;font-weight:500;line-height:1.45;padding-top:7px}
.ticket-box .donor{color:var(--blue-deep)}
.outlets{left:0;top:935px;width:808px;height:96px;background:var(--light);border-top:3px solid var(--blue)}
.outlets-tab{left:230px;top:935px;width:335px;height:30px;background:var(--blue);color:var(--white);
  font-weight:700;font-size:17.5px;text-align:center;line-height:30px;
  clip-path:polygon(0 0,100% 0,93% 100%,7% 100%)}
.outlet{top:983px;display:flex;gap:8px}
.outlet svg{flex:none;margin-top:1px}
.outlet b{display:block;font-size:14.5px;font-weight:700;color:var(--ink)}
.outlet span{display:block;font-size:11px;color:var(--ink);margin-top:2px}
.outlet-div{top:985px;width:1px;height:36px;background:#b9b9b9}
.contacts{left:402px;top:1031px;width:406px;height:111px;background:var(--dark);color:var(--white)}
.contacts h4{position:absolute;left:32px;top:18px;font-size:15px;font-weight:800;letter-spacing:.2px}
.contacts .line{position:absolute;left:205px;top:27px;width:170px;height:1px;background:#9a9a9a}
.person{position:absolute;top:48px;display:flex;gap:10px;align-items:center}
.person .icon{width:31px;height:31px;border-radius:6px;background:var(--blue);display:flex;align-items:center;justify-content:center}
.person b{display:block;font-size:14px;font-weight:800}
.person span{display:block;font-size:14px;font-weight:500}
.social{left:30px;top:1033px;width:369px;height:90px;background:var(--blue);border-radius:12px;display:flex;align-items:center;gap:22px;padding-left:13px}
.social .mark{width:63px;height:63px;border:3px solid var(--white);border-radius:12px;flex:none}
.social p{color:var(--white);font-weight:800;font-size:16.5px;line-height:1.28}
</style>
</head>
<body>
<main class="flyer">
  <div class="abs band-left"></div>
  <div class="abs band-right"></div>

  <div class="abs venue-photo" role="img" aria-label="Photo of the white clapboard community center with a blue metal roof under a summer sky"></div>

  <header class="abs title-panel">
    <p class="presents">THE FERNWICK COMMUNITY CENTER PRESENTS</p>
    <h1 class="title"><span class="lead">THE FIRST ANNUAL</span><span class="name">FERNWICK LEGACY</span><span class="name">GALA</span></h1>
  </header>

  <svg class="abs wave" viewBox="0 0 808 180" aria-hidden="true">
    <path d="M0 100 C110 40 250 20 420 95 C560 150 700 70 808 25 L808 180 L0 180 Z" fill="#d5d5d5"/>
    <path d="M0 92 C120 40 250 28 420 100 C560 156 700 82 808 40 L808 180 L0 180 Z" fill="var(--blue)"/>
    <path d="M0 108 C130 60 250 52 420 112 C560 162 700 92 808 60 L808 180 L0 180 Z" fill="var(--white)"/>
  </svg>

  <svg class="abs date-badge" viewBox="0 0 268 268" aria-hidden="true">
    <defs><clipPath id="badgeClip"><circle cx="134" cy="134" r="122"/></clipPath></defs>
    <circle cx="134" cy="134" r="134" fill="var(--white)"/>
    <g clip-path="url(#badgeClip)">
      <rect width="268" height="268" fill="var(--blue)"/>
      <rect y="150" width="268" height="84" fill="var(--dark)"/>
    </g>
  </svg>
  <div class="abs date-text">
    <div class="day">APRIL 23</div>
    <div class="year">2022</div>
    <div class="time">STARTING AT<br>5:00 PM WITH<br>COCKTAIL HOUR</div>
  </div>

  <h2 class="abs headline">LIVE AUCTION, SILENT AUCTION, RAFFLE AND A CASH BAR!</h2>
  <div class="abs rule"></div>
  <div class="abs body-copy">
    <p>Come on out to the Fernwick Community Center for a delicious prime rib dinner, drinks, entertainment and more! There will be plenty of amazing auction items for everyone to choose from.</p>
    <p>All proceeds will go to the Fernwick Community Center. We will share some history of the school and each year we will highlight a local family. This year will be the Harlow family who have been here for ....years!!</p>
    <p>High Side Barn, dirt bike, custom knives, a pack trip and so much more!</p>
  </div>

  <section class="abs ticket-box">
    <div class="price"><small>TICKETS FOR THE EVENT ARE</small><strong>$50 EACH OR<br>$90 FOR A COUPLE</strong></div>
    <div class="raffle">Tickets For The 10x12 High Side Barn<br>$25 Each Or 5 For $100.<br><span class="donor">Donated By: Ridgeline Shed Center Of<br>Alder Falls, Value $6500</span></div>
  </section>

  <div class="abs outlets"></div>
  <div class="abs outlets-tab">GET YOUR TICKETS FROM</div>

  <div class="abs outlet" style="left:38px">
    <svg width="16" height="20" viewBox="0 0 16 20"><path d="M8 0a8 8 0 0 1 8 8c0 6-8 12-8 12S0 14 0 8a8 8 0 0 1 8-8z" fill="var(--blue)"/><circle cx="8" cy="8" r="3" fill="var(--light)"/></svg>
    <div><b>Ridgeline Shed Center in Alder Falls</b><span>48 Harrow Rd, Alder Falls</span></div>
  </div>
  <div class="abs outlet-div" style="left:322px"></div>
  <div class="abs outlet" style="left:337px">
    <svg width="16" height="20" viewBox="0 0 16 20"><path d="M8 0a8 8 0 0 1 8 8c0 6-8 12-8 12S0 14 0 8a8 8 0 0 1 8-8z" fill="var(--blue)"/><circle cx="8" cy="8" r="3" fill="var(--light)"/></svg>
    <div><b>Tallpine Real Estate</b><span>212 E Cedar St, Alder Falls</span></div>
  </div>
  <div class="abs outlet-div" style="left:580px"></div>
  <div class="abs outlet" style="left:598px">
    <svg width="16" height="20" viewBox="0 0 16 20"><path d="M8 0a8 8 0 0 1 8 8c0 6-8 12-8 12S0 14 0 8a8 8 0 0 1 8-8z" fill="var(--blue)"/><circle cx="8" cy="8" r="3" fill="var(--light)"/></svg>
    <div><b>Fernwick Store</b><span>6150 County Road 40, Fernwick</span></div>
  </div>

  <section class="abs contacts">
    <h4>OR GET THEM FROM</h4>
    <div class="line"></div>
    <div class="person" style="left:35px">
      <div class="icon"><svg width="17" height="17" viewBox="0 0 24 24"><path d="M6.6 10.8a15.2 15.2 0 0 0 6.6 6.6l2.2-2.2c.3-.3.7-.4 1-.2 1.1.4 2.3.6 3.6.6.6 0 1 .4 1 1V20c0 .6-.4 1-1 1A17 17 0 0 1 3 4c0-.6.4-1 1-1h3.5c.6 0 1 .4 1 1 0 1.3.2 2.5.6 3.6.1.3 0 .7-.2 1z" fill="var(--white)"/></svg></div>
      <div><b>MARLA QUINT</b><span>(555) 210-4418</span></div>
    </div>
    <div class="person" style="left:208px">
      <div class="icon"><svg width="17" height="17" viewBox="0 0 24 24"><path d="M6.6 10.8a15.2 15.2 0 0 0 6.6 6.6l2.2-2.2c.3-.3.7-.4 1-.2 1.1.4 2.3.6 3.6.6.6 0 1 .4 1 1V20c0 .6-.4 1-1 1A17 17 0 0 1 3 4c0-.6.4-1 1-1h3.5c.6 0 1 .4 1 1 0 1.3.2 2.5.6 3.6.1.3 0 .7-.2 1z" fill="var(--white)"/></svg></div>
      <div><b>DANA HOLLOWAY</b><span>(555) 287-6093</span></div>
    </div>
  </section>

  <section class="abs social">
    <div class="mark"></div>
    <p>Follow the Fernwick Community Center's Commons page to see all the auction items available!</p>
  </section>
</main>
</body>
</html>
```